Bref créative
Stationary Project
BRQ - Bright Rivers Quality
Simple
Dale Morrow
Pine Hollow, PH
dmorrow@br-quality.example
brightriversquality.example
Industry Type is for Photography. For some reason it does not show when I confirm brief. Add "Bringing Nature Indoors" to project. This font style can be different than the BRQ Logo Font. (possibly script, but must be crisp and clear). Can use color but must not distract from Falcon Image. Also at this point in time, name, email, etc should be in the same font as the Logo but may possibly be changed once designs are submitted and reviewed by my staff.

```html
<!DOCTYPE html>
<html lang="en">
<head>
<meta charset="utf-8">
<title>BRQ - Bright Rivers Quality Stationery</title>
<link href="https://fonts.googleapis.com/css2?family=Cormorant+Garamond:wght@600&display=swap" rel="stylesheet">
<style>
  :root{
    --stage:#2a2a2c;
    --paper:#ffffff;
    --gold:#d3b878;
    --ink:#141414;
    --muted:#555555;
    --fold:#d8d8d8;
  }
  html,body{margin:0;padding:0;overflow:hidden}
  body{width:1200px;height:677px;background:var(--stage);position:relative;font-family:"Cormorant Garamond",Georgia,serif;color:var(--ink)}
  .piece{position:absolute;background:var(--paper);overflow:hidden;box-shadow:0 2px 6px rgba(0,0,0,.45)}
  .piece svg.art{position:absolute;inset:0;width:100%;height:100%}
  .mark{position:absolute;display:flex;align-items:center;gap:4px;font-weight:600;color:var(--ink);line-height:1;white-space:nowrap}
  .mark .dot{border-radius:50%;background:var(--ink);flex:none}
  .mark .name{display:flex;flex-direction:column}
  .mark .init{letter-spacing:.06em}
  .mark .full{letter-spacing:.08em;text-transform:uppercase}
  .small-print{position:absolute;font-weight:600;color:var(--muted);white-space:nowrap;line-height:1.6}

  /* business cards */
  .card-front{left:173px;top:139px;width:139px;height:84px}
  .card-front .mark{left:14px;top:20px}
  .card-front .mark .dot{width:14px;height:14px}
  .card-front .init{font-size:13px}
  .card-front .full{font-size:4.5px}
  .card-gold{left:173px;top:245px;width:139px;height:67px;background:var(--gold)}
  .card-white{left:173px;top:365px;width:139px;height:79px}
  .centered{left:50%;top:50%;transform:translate(-50%,-50%)}
  .centered .dot{width:14px;height:14px}
  .centered .init{font-size:15px}

  /* letterhead */
  .letterhead{left:365px;top:101px;width:336px;height:432px}
  .letterhead .mark{left:22px;top:30px}
  .letterhead .mark .dot{width:24px;height:24px}
  .letterhead .init{font-size:22px}
  .letterhead .full{font-size:7px;margin-top:2px}
  .letterhead .small-print{right:20px;bottom:12px;font-size:5px;text-align:right}

  /* envelopes */
  .envelope-front{left:742px;top:96px;width:331px;height:156px}
  .envelope-front .mark{left:20px;top:22px}
  .envelope-front .mark .dot{width:18px;height:18px}
  .envelope-front .init{font-size:17px}
  .envelope-front .full{font-size:5.5px;margin-top:2px}
  .envelope-front .small-print{left:20px;top:74px;font-size:5px}

  .envelope-back .mark{left:50%;transform:translateX(-50%)}
  .envelope-back .mark .dot{width:14px;height:14px}
  .envelope-back .init{font-size:14px}
  .env-gold{left:746px;top:296px;width:346px;height:120px}
  .env-gold .mark{top:20px}
  .env-black{left:773px;top:367px;width:331px;height:120px}
  .env-black .mark{top:28px;color:var(--paper)}
  .env-black .mark .dot{background:var(--paper)}
  .env-white{left:809px;top:446px;width:309px;height:106px}
  .env-white .mark{top:20px}
</style>
</head>
<body>

<!-- business card: front -->
<div class="piece card-front">
  <svg class="art" viewBox="0 0 139 84" preserveAspectRatio="none">
    <path d="M70 0 H139 V34 C125 14 100 4 70 0 Z" fill="var(--gold)"/>
    <path d="M78 0 C105 5 126 16 139 34 V40 C124 20 104 8 78 0 Z" fill="var(--ink)"/>
    <path d="M0 64 C30 72 60 78 95 84 H0 Z" fill="var(--gold)"/>
  </svg>
  <div class="mark"><span class="dot"></span><span class="name"><span class="init">BRQ</span><span class="full">Bright Rivers Quality</span></span></div>
</div>

<!-- business card: gold back -->
<div class="piece card-gold">
  <div class="mark centered"><span class="dot"></span><span class="init">BRQ</span></div>
</div>

<!-- business card: white back -->
<div class="piece card-white">
  <div class="mark centered"><span class="dot"></span><span class="init">BRQ</span></div>
</div>

<!-- letterhead -->
<div class="piece letterhead">
  <svg class="art" viewBox="0 0 336 432" preserveAspectRatio="none">
    <path d="M150 0 H336 V72 C290 28 220 6 150 0 Z" fill="var(--gold)"/>
    <path d="M165 0 C235 8 300 34 336 72 V86 C296 42 235 12 165 0 Z" fill="var(--ink)"/>
    <path d="M0 400 C60 412 120 424 190 432 H0 Z" fill="var(--gold)"/>
  </svg>
  <div class="mark"><span class="dot"></span><span class="name"><span class="init">BRQ</span><span class="full">Bright Rivers Quality</span></span></div>
  <div class="small-print">12 Heron Way, Pine Hollow, PH 10234<br>T: (555) 010-2234 | dmorrow@br-quality.example | brightriversquality.example</div>
</div>

<!-- envelope: front -->
<div class="piece envelope-front">
  <svg class="art" viewBox="0 0 331 156" preserveAspectRatio="none">
    <path d="M200 0 H331 V64 C300 30 255 8 200 0 Z" fill="var(--gold)"/>
    <path d="M212 0 C260 8 305 30 331 64 V74 C302 38 260 12 212 0 Z" fill="var(--ink)"/>
  </svg>
  <div class="mark"><span class="dot"></span><span class="name"><span class="init">BRQ</span><span class="full">Bright Rivers Quality</span></span></div>
  <div class="small-print">12 Heron Way, Pine Hollow, PH 10234</div>
</div>

<!-- envelope backs, stacked -->
<div class="piece envelope-back env-gold">
  <svg class="art" viewBox="0 0 346 120" preserveAspectRatio="none">
    <path d="M0 0 H346 V12 L200 52 Q173 60 146 52 L0 12 Z" fill="var(--gold)"/>
  </svg>
  <div class="mark"><span class="dot"></span><span class="init">BRQ</span></div>
</div>

<div class="piece envelope-back env-black">
  <svg class="art" viewBox="0 0 331 120" preserveAspectRatio="none">
    <path d="M0 0 H331 V14 L192 66 Q165.5 76 139 66 L0 14 Z" fill="var(--ink)"/>
  </svg>
  <div class="mark"><span class="dot"></span><span class="init">BRQ</span></div>
</div>

<div class="piece envelope-back env-white">
  <svg class="art" viewBox="0 0 309 106" preserveAspectRatio="none">
    <path d="M0 0 L130 52 Q154.5 60 179 52 L309 0" fill="none" stroke="var(--fold)" stroke-width="1"/>
  </svg>
  <div class="mark"><span class="dot"></span><span class="init">BRQ</span></div>
</div>

</body>
</html>
```